Re-design existing website and add products for sale.

Our current website is very basic and cluttered. (emberfernwellness.com.au)We want a modern looking website that is easy to navigate. We also want to start selling essential oils and crystal products, so there needs to be a separate page for this. Also needs to be easily edited as we need to change the monthly oracle card with the description. Would like calming colours as we are all about natural healing. Alongside the services listed there should be a button to book now which asks for their name, email, phone number ect. and adds it to the cart.

• Logo is still being designed, please leave a space for the logo which will basically be a lotus flower within a mandala.

```html
<!DOCTYPE html>
<html lang="en">
<head>
<meta charset="utf-8">
<title>Crystal Product Card</title>
<link href="https://fonts.googleapis.com/css2?family=Raleway:wght@400;700&family=Montserrat:wght@700&display=swap" rel="stylesheet">
<style>
  :root {
    --sky-light: #74b6d8;
    --sky-deep: #1b8ec6;
    --cyan: #08c6f2;
    --card-blue: #72b5d6;
    --white: #ffffff;
    --ink: #111111;
    --muted: #7a6e6e;
    --coral: #f85f62;
    --star: #f6b23c;
    --chocolate: #4a2222;
    --amber: #f6b23c;
    --periwinkle: #5f86e0;
    --orange: #f7941d;
    --border: #8a7c7c;
  }
  * { margin: 0; padding: 0; box-sizing: border-box; }
  html, body { width: 1200px; height: 675px; overflow: hidden; }
  body {
    position: relative;
    font-family: "Raleway", sans-serif;
    background:
      radial-gradient(ellipse at 100% 50%, var(--cyan) 0%, rgba(8,198,242,0) 70%),
      linear-gradient(160deg, var(--sky-light) 0%, var(--sky-deep) 100%);
  }
  .product-media {
    position: absolute; left: 154px; top: 88px; width: 342px; height: 498px;
    background: var(--card-blue);
    border-radius: 38px;
    box-shadow: -6px 14px 34px rgba(10, 90, 60, 0.55);
    z-index: 2;
  }
  .product-photo {
    position: absolute; left: 26px; top: 176px; width: 262px; height: 152px;
    border-radius: 14px;
    background: linear-gradient(180deg, #c9d5dc 0%, #a9b8c1 60%, #5f7d8e 100%);
    opacity: 0.85;
  }
  .product-details {
    position: absolute; left: 496px; top: 118px; width: 626px; height: 438px;
    background: var(--white);
    box-shadow: 0 10px 30px rgba(10, 90, 80, 0.35);
    z-index: 1;
  }
  .product-name {
    position: absolute; left: 61px; top: 42px;
    font-size: 30px; font-weight: 700; color: var(--ink); letter-spacing: -0.2px;
  }
  .rating { position: absolute; left: 61px; top: 88px; display: flex; align-items: center; gap: 6px; }
  .rating svg { width: 24px; height: 24px; fill: var(--star); }
  .rating-count { font-size: 17px; font-weight: 700; color: var(--muted); margin-left: 2px; }
  .price {
    position: absolute; left: 60px; top: 124px;
    font-family: "Montserrat", sans-serif; font-weight: 700; font-size: 45px;
    color: var(--coral); word-spacing: 10px;
  }
  .swatches { position: absolute; left: 62px; top: 198px; height: 44px; width: 260px; }
  .swatch { position: absolute; top: 6px; width: 32px; height: 32px; border-radius: 50%; }
  .swatch--coral { left: 0; background: var(--coral); }
  .swatch--chocolate { left: 48px; background: var(--chocolate); }
  .swatch--amber { left: 100px; background: var(--amber); }
  .swatch--periwinkle { left: 150px; background: var(--periwinkle); }
  .swatch-ring {
    position: absolute; left: 93px; top: -1px; width: 46px; height: 46px;
    border-radius: 50%; border: 2px solid #9a9090;
  }
  .select-size {
    position: absolute; left: 68px; top: 262px; width: 111px; height: 40px;
    border: 2px solid var(--border); border-radius: 6px;
    display: flex; align-items: center; justify-content: space-between; padding: 0 18px 0 20px;
    font-size: 22px; color: var(--ink);
  }
  .caret { font-size: 12px; color: #777; }
  .select-qty {
    position: absolute; left: 206px; top: 262px; width: 112px; height: 40px;
    border: 2px solid var(--border); border-radius: 6px; display: flex; overflow: hidden;
  }
  .qty-label {
    width: 55px; background: var(--orange); color: var(--white);
    font-size: 22px; display: flex; align-items: center; justify-content: center;
  }
  .qty-value {
    flex: 1; display: flex; align-items: center; justify-content: center; gap: 6px;
    font-size: 20px; color: var(--ink);
  }
  .add-to-cart {
    position: absolute; left: 62px; top: 340px; width: 187px; height: 41px;
    background: var(--coral); color: var(--white); border-radius: 5px;
    font-size: 22px; display: flex; align-items: center; justify-content: center;
  }
  .checkout-link {
    position: absolute; left: 269px; top: 350px; font-size: 14.5px; color: var(--muted);
  }
</style>
</head>
<body>
  <div class="product-media">
    <div class="product-photo" role="img" aria-label="Cut crystal candle holders and business card holder"></div>
  </div>

  <section class="product-details">
    <h1 class="product-name">Your Crystal product Name</h1>
    <div class="rating">
      <svg viewBox="0 0 24 24"><path d="M12 1.5l3.1 7 7.4.6-5.6 4.9 1.7 7.4L12 17.5l-6.6 3.9 1.7-7.4L1.5 9.1l7.4-.6z"/></svg>
      <svg viewBox="0 0 24 24"><path d="M12 1.5l3.1 7 7.4.6-5.6 4.9 1.7 7.4L12 17.5l-6.6 3.9 1.7-7.4L1.5 9.1l7.4-.6z"/></svg>
      <svg viewBox="0 0 24 24"><path d="M12 1.5l3.1 7 7.4.6-5.6 4.9 1.7 7.4L12 17.5l-6.6 3.9 1.7-7.4L1.5 9.1l7.4-.6z"/></svg>
      <svg viewBox="0 0 24 24"><path d="M12 1.5l3.1 7 7.4.6-5.6 4.9 1.7 7.4L12 17.5l-6.6 3.9 1.7-7.4L1.5 9.1l7.4-.6z"/></svg>
      <svg viewBox="0 0 24 24"><path d="M12 1.5l3.1 7 7.4.6-5.6 4.9 1.7 7.4L12 17.5l-6.6 3.9 1.7-7.4L1.5 9.1l7.4-.6z"/></svg>
      <span class="rating-count">(60)</span>
    </div>
    <p class="price">USD $66</p>
    <div class="swatches">
      <span class="swatch swatch--coral"></span>
      <span class="swatch swatch--chocolate"></span>
      <span class="swatch-ring"></span>
      <span class="swatch swatch--amber"></span>
      <span class="swatch swatch--periwinkle"></span>
    </div>
    <div class="select-size">Size <span class="caret">▼</span></div>
    <div class="select-qty">
      <span class="qty-label">QTY</span>
      <span class="qty-value">1 <span class="caret">▼</span></span>
    </div>
    <div class="add-to-cart">Add to Cart</div>
    <span class="checkout-link">Checkout with SwiftPurse</span>
  </section>
</body>
</html>
```